Corvant Systems Business Card

Create an appealing and elegant Business card for corvant systems. Include logo and use related colors from website, be creative. Include Business name, my name, tile, address, contacts, address, and social media contacts if possible. Logo PSD file is attached.

Bleed Area: 3.46" x 2.32"
Trim: 3.3" x 2.16"
Safe Area: 3.14" x 2.02"

Save files as vector-based PDF with outlined text and PNG.
No crop marks
CMYK color setting

Business Card Info:

Corvant Systems

Dennis Halvorsen
Owner

512 Brindlemoor Rd Unit C
Alderbrook, ME 02871
t. 1.888.555.0162
e. dennis.h@corvantsys.example
w. www.corvantsys.example

facebook. www.facebook.com/CorvantSys
twitter. twitter.com/corvantsys
pinterest. www.pinterest.com/corvantsys/

Target Market(s)

Business Owners and Partners

Industry/Entity Type

Business

Requirements
Must have
• Logo and related colors from website

```html
<!DOCTYPE html>
<html lang="en">
<head>
<meta charset="utf-8">
<title>Corvant Systems – Business Card</title>
<link rel="stylesheet" href="https://fonts.googleapis.com/css2?family=Open+Sans:wght@400;600;700&display=swap">
<style>
  :root {
    --card-bg: #aaa597;
    --band-blue: #4f78ae;
    --ink: #1f1f1f;
    --ink-soft: #262626;
    --white: #ffffff;
  }
  html, body {
    margin: 0;
    padding: 0;
    width: 724px;
    height: 1200px;
    overflow: hidden;
    background: var(--card-bg);
  }
  .card {
    position: relative;
    width: 724px;
    height: 1200px;
    background: var(--card-bg);
    font-family: "Open Sans", Arial, sans-serif;
    color: var(--ink);
  }
  .brand {
    position: absolute;
    left: 120px;
    top: 108px;
    margin: 0;
    font-weight: 600;
    color: var(--ink);
  }
  .brand-line {
    display: block;
    line-height: 1.05;
  }
  .brand-primary {
    font-size: 76px;
    letter-spacing: 2px;
  }
  .brand-secondary {
    font-size: 62px;
    margin-top: 4px;
  }
  .name-band {
    position: absolute;
    left: 0;
    top: 500px;
    width: 724px;
    height: 181px;
    background: var(--band-blue);
  }
  .person-name {
    position: absolute;
    left: 150px;
    top: 44px;
    margin: 0;
    font-size: 50px;
    font-weight: 600;
    color: var(--ink);
    line-height: 1;
  }
  .person-title {
    position: absolute;
    left: 150px;
    top: 110px;
    margin: 0;
    font-size: 36px;
    font-weight: 400;
    color: var(--white);
    line-height: 1;
  }
  .contact-block,
  .social-block {
    position: absolute;
    left: 116px;
    margin: 0;
    font-size: 24px;
    line-height: 33px;
    color: var(--ink-soft);
    font-style: normal;
  }
  .contact-block { top: 770px; }
  .social-block { top: 952px; }
  .contact-block span,
  .social-block span { display: block; }
</style>
</head>
<body>
  <div class="card">
    <h1 class="brand">
      <span class="brand-line brand-primary">CORVANT</span>
      <span class="brand-line brand-secondary">Systems</span>
    </h1>

    <section class="name-band">
      <h2 class="person-name">Dennis Halvorsen</h2>
      <p class="person-title">Owner</p>
    </section>

    <address class="contact-block">
      <span>512 Brindlemoor Rd Unit C</span>
      <span>Alderbrook, ME 02871</span>
      <span>t. 1.888.555.0162</span>
      <span>e. dennis.h@corvantsys.example</span>
      <span>w. www.corvantsys.example</span>
    </address>

    <p class="social-block">
      <span>facebook. www.facebook.com/CorvantSys</span>
      <span>twitter. twitter.com/corvantsys</span>
      <span>pinterest. www.pinterest.com/corvantsys/</span>
    </p>
  </div>
</body>
</html>
```